New name flyer

We have just changed our business name from kR Property group to Harbour Lantern. We want to distribute a flyer to the local community to inform them of the change. We are a realestate agency which focuses mainly on property management but also sales. We service from Brisbane to the Sunshine coast.

Target Market(s)

Local community

Industry/Entity Type

realestate

Requirements
Must have
• Details of name change
Nice to have
• Servicing area Brisbane and Sunshine Coast, no change in management or services we offer, and will continue pride ourselves on offering a high level of service, with the same team from the Gold to Sunshine Coast.
Should not have
• too much wording.

```html
<!DOCTYPE html>
<html lang="en">
<head>
<meta charset="utf-8">
<title>Harbour Lantern – New Name Flyer</title>
<link rel="stylesheet" href="https://fonts.googleapis.com/css2?family=Montserrat:wght@500;700;800;900&display=swap">
<style>
  :root {
    --navy: #0d2f68;
    --gold: #d19a2c;
    --red: #e3202a;
    --white: #ffffff;
    --backdrop: #9b9b9b;
    --photo-deep: #0b2a78;
    --photo-mid: #1340a8;
    --band-gold: #c98a22;
  }
  * { margin: 0; padding: 0; box-sizing: border-box; }
  html, body { width: 919px; height: 1200px; overflow: hidden; }
  body {
    background: var(--backdrop);
    font-family: "Montserrat", Arial, sans-serif;
    position: relative;
  }
  .flyer {
    position: absolute;
    left: 47px; top: 18px;
    width: 824px; height: 1163px;
    background: var(--white);
    overflow: hidden;
  }
  .header-area {
    position: absolute; left: 0; top: 0; width: 100%; height: 297px;
    background: linear-gradient(135deg, #f1f1f1 0%, #ffffff 45%, #f0f0f0 100%);
  }
  .headline {
    position: absolute; left: 0; width: 100%;
    text-align: center; font-weight: 800; font-size: 41px;
    line-height: 1; letter-spacing: -0.3px;
  }
  .headline--navy { top: 63px; color: var(--navy); }
  .headline--gold { top: 120px; color: var(--gold); }
  .name-tag {
    position: absolute; top: 190px; height: 41px; width: 309px;
    color: var(--white); font-weight: 700; font-size: 27px;
    display: flex; align-items: center; justify-content: center;
    white-space: nowrap;
  }
  .name-tag--old { left: 68px; background: var(--red); }
  .name-tag--new { left: 446px; background: var(--navy); }
  .name-tag__to {
    position: absolute; left: 388px; top: 185px;
    width: 48px; height: 48px; border-radius: 50%;
    background: var(--gold); color: var(--white);
    font-weight: 800; font-size: 21px;
    display: flex; align-items: center; justify-content: center;
  }
  .hero-photo {
    position: absolute; left: 0; top: 297px; width: 100%; height: 555px;
    background: linear-gradient(160deg, var(--photo-mid) 0%, var(--photo-deep) 55%, #1a3f9a 100%);
  }
  .brand-name {
    position: absolute; left: 0; top: 535px; width: 100%;
    text-align: center; color: var(--white);
    font-family: "Montserrat", Arial, sans-serif;
    font-weight: 800; font-size: 62px; line-height: 80px;
    white-space: nowrap;
  }
  .service-band {
    position: absolute; left: 0; top: 852px; width: 100%; height: 200px;
    background: linear-gradient(100deg, #b97d1d 0%, var(--band-gold) 50%, #b57a1f 100%);
  }
  .service-band__title {
    position: absolute; left: 0; top: 875px; width: 100%;
    text-align: center; color: var(--white);
    font-weight: 900; font-size: 29px; line-height: 42px;
  }
  .service-band__text {
    position: absolute; left: 117px; top: 964px; width: 590px;
    text-align: center; color: var(--white);
    font-weight: 500; font-size: 14.5px; line-height: 22px;
  }
  .footer-area {
    position: absolute; left: 0; top: 1052px; width: 100%; height: 111px;
    background: linear-gradient(180deg, #eeeeee 0%, #f7f7f7 60%, #ececec 100%);
  }
  .contact {
    position: absolute; top: 1084px; height: 44px;
    display: flex; align-items: center;
  }
  .contact--phone { left: 77px; }
  .contact--web { left: 377px; }
  .contact__icon {
    width: 29px; height: 29px; border-radius: 50%;
    background: var(--gold);
    display: flex; align-items: center; justify-content: center;
    margin-right: 8px;
  }
  .contact__phone {
    color: var(--navy); font-weight: 800; font-size: 34px; letter-spacing: -0.5px;
  }
  .contact__web { color: var(--navy); font-weight: 500; font-size: 21px; }
  .contact__web em { font-style: normal; color: var(--gold); }
  .contact-divider {
    position: absolute; left: 366px; top: 1088px; width: 1.5px; height: 34px;
    background: var(--navy);
  }
</style>
</head>
<body>
  <main class="flyer">
    <section class="header-area">
      <h1 class="headline headline--navy">WE HAVE JUST CHANGED</h1>
      <h2 class="headline headline--gold">OUR BUSINESS NAME FROM</h2>
      <div class="name-tag name-tag--old">kR Property group</div>
      <div class="name-tag__to">To</div>
      <div class="name-tag name-tag--new">Harbour Lantern</div>
    </section>

    <div class="hero-photo" role="img" aria-label="Photo of a modern two-storey home with glass balustrades at dusk, tinted blue"></div>
    <div class="brand-name">Harbour Lantern</div>

    <section class="service-band" role="img" aria-label="Photo of the home's timber deck and pool, tinted gold"></section>
    <h3 class="service-band__title">Servicing area Brisbane and<br>Sunshine Coast</h3>
    <p class="service-band__text">No change in management or services we offer, and will continue pride ourselves on offering a high level of service, with the same team from the Gold to Sunshine Coast.</p>

    <footer class="footer-area" role="img" aria-label="Faint light photo of a pool edge"></footer>
    <div class="contact contact--phone">
      <span class="contact__icon">
        <svg width="17" height="17" viewBox="0 0 24 24" fill="#fff"><path d="M6.6 10.8a15.1 15.1 0 0 0 6.6 6.6l2.2-2.2a1 1 0 0 1 1-.25 11.4 11.4 0 0 0 3.6.57 1 1 0 0 1 1 1V20a1 1 0 0 1-1 1A17 17 0 0 1 3 4a1 1 0 0 1 1-1h3.5a1 1 0 0 1 1 1c0 1.25.2 2.45.57 3.57a1 1 0 0 1-.25 1z"/></svg>
      </span>
      <span class="contact__phone">07 3555 0182</span>
    </div>
    <div class="contact-divider"></div>
    <div class="contact contact--web">
      <span class="contact__icon">
        <svg width="19" height="19" viewBox="0 0 24 24" fill="none" stroke="#fff" stroke-width="1.6"><circle cx="12" cy="12" r="9"/><ellipse cx="12" cy="12" rx="4" ry="9"/><path d="M3 12h18M4.5 7.5h15M4.5 16.5h15"/></svg>
      </span>
      <span class="contact__web">www.<em>harbourlantern</em>.com.au</span>
    </div>
  </main>
</body>
</html>
```